Zielgruppe
Ich zeige Frauen 35+ wie sie ihren Traummann finden können, ohne im Internet nach ihm zu suchen. Meine Zielgruppe sind meist Frauen, die schon lange Single sind und doch voller Sehnsucht nach einem Partner. Diese Frauen haben oft negative Erfolgsverhinderer-Glaubenssätze ('In meinem Alter gibt es keine guten Männer mehr', 'Ich bin zu dick - Männer wollen schlanke Frauen'...). Ich zeige diesen Frauen, wie sie durch eine andere Einstellung in kurzer Zeit ihren Herzenspartner ins Leben ziehen können.
Aufgabenstellung
Die Menschen, die dieses Buch lesen, sind normalerweise weiblich und mindestens 35 Jahre alt, eher älter. Das Cover sollte also Frauen ansprechen, die sich ihren Traummann wünschen und darf gerne auch 'weibliche' Farbtöne wie rot und rosa, pink etc. enthalten (das sind auch 'meine' Business-Farben). Es ist aber nur eine Idee von mir, keine Vorgabe. Ich bin offen für alles.

```html
<!DOCTYPE html>
<html lang="de">
<head>
<meta charset="utf-8">
<title>Wer loslässt, der gewinnt – Buchcover</title>
<link rel="stylesheet" href="https://fonts.googleapis.com/css2?family=Dancing+Script:wght@700&family=Heebo:wght@300;700&display=swap">
<style>
  :root {
    --bg-pink: #f6cccc;
    --bg-pink-light: #f9dcdb;
    --petal: #ee8f93;
    --petal-soft: #f3b1b3;
    --title-red: #d84b52;
    --gold: #d9b44a;
    --white: #ffffff;
    --mark-red: #7a1020;
  }
  html, body { margin: 0; padding: 0; overflow: hidden; }
  body { width: 750px; height: 1200px; background: var(--bg-pink); }
  .cover {
    position: relative; width: 750px; height: 1200px; overflow: hidden;
    background: linear-gradient(160deg, var(--bg-pink-light) 0%, var(--bg-pink) 55%, #f4c4c4 100%);
    font-family: "Heebo", sans-serif;
  }
  .art { position: absolute; }
  .flowers-top-left {
    left: -40px; top: -20px; width: 360px; height: 380px;
    background: radial-gradient(ellipse at 45% 45%, var(--petal) 0%, var(--petal-soft) 40%, rgba(243,177,179,0) 72%);
  }
  .flower-top-center {
    left: 280px; top: 10px; width: 230px; height: 190px;
    background: radial-gradient(ellipse at 50% 60%, var(--petal) 0%, var(--petal-soft) 40%, rgba(243,177,179,0) 72%);
  }
  .magnolia-bottom-right {
    left: 380px; top: 730px; width: 380px; height: 290px;
    background: radial-gradient(ellipse at 65% 55%, var(--petal) 0%, var(--petal-soft) 38%, rgba(243,177,179,0) 72%);
  }
  .hearts-watercolor {
    left: 170px; top: 930px; width: 270px; height: 190px;
    background: radial-gradient(ellipse at 50% 50%, #f2a3a6 0%, rgba(242,163,166,0.6) 45%, rgba(242,163,166,0) 72%);
  }
  .rings { position: absolute; inset: 0; }
  .title-disc {
    position: absolute; left: 34px; top: 180px; width: 678px; height: 678px;
    border-radius: 50%; background: var(--white);
    box-shadow: 0 10px 22px rgba(150, 90, 100, 0.35), -4px 4px 8px rgba(120,120,130,0.25);
  }
  .author, .title-line, .subtitle { position: absolute; left: 0; width: 750px; text-align: center; color: var(--title-red); margin: 0; }
  .author { top: 232px; font-weight: 300; font-size: 26px; letter-spacing: 0.2px; }
  .title { margin: 0; font-family: "Dancing Script", cursive; font-weight: 700; }
  .title-line { font-size: 138px; line-height: 1; -webkit-text-stroke: 2px var(--title-red); }
  .line-1 { top: 270px; left: 12px; }
  .line-2 { top: 396px; left: 6px; }
  .line-3 { top: 524px; left: 8px; }
  .subtitle { top: 708px; font-weight: 300; font-size: 32px; line-height: 36px; }
  .imprint {
    position: absolute; left: 498px; top: 1094px;
    display: flex; align-items: center; gap: 8px;
    font-family: "Heebo", sans-serif; font-weight: 700; font-size: 30px; color: var(--mark-red);
  }
  .imprint-dot { width: 14px; height: 14px; border-radius: 50%; background: var(--mark-red); }
</style>
</head>
<body>
<main class="cover">
  <div class="art flowers-top-left" role="img" aria-label="Aquarellierte rosa Blüten mit feinen Linien und goldenem Blütenkern"></div>
  <div class="art flower-top-center" role="img" aria-label="Rosa Aquarellblüte mit goldenem Kern"></div>
  <div class="art magnolia-bottom-right" role="img" aria-label="Rosa Magnolienzweig mit goldenen Knospen und Blättern"></div>
  <div class="art hearts-watercolor" role="img" aria-label="Zwei sich überlappende rosa Aquarellherzen"></div>

  <svg class="rings" width="750" height="1200" viewBox="0 0 750 1200" aria-hidden="true">
    <circle cx="144" cy="843" r="136" fill="none" stroke="var(--gold)" stroke-width="1.5"/>
  </svg>

  <div class="title-disc"></div>

  <svg class="rings" width="750" height="1200" viewBox="0 0 750 1200" aria-hidden="true">
    <circle cx="388" cy="506" r="343" fill="none" stroke="var(--gold)" stroke-width="2"/>
  </svg>

  <p class="author">Carla Wendt-Oberhofer</p>
  <h1 class="title">
    <span class="title-line line-1">Wer</span>
    <span class="title-line line-2">loslässt,</span>
    <span class="title-line line-3">der gewinnt</span>
  </h1>
  <p class="subtitle">Warum die große Liebe kommt,<br>wenn du sie nicht<br>mehr jagst</p>

  <div class="imprint"><span class="imprint-dot"></span>lovebound</div>
</main>
</body>
</html>
```